KTR Vials

Sales Sheet (2-Sided) 8 1/2 x 11 Size
Company Sells Prescription Vials and Toner to Pharmacies

Sales Sheet
Side ONE (FRONT)
Graphic: KTR Services Logo Text: Quality Vials without the Premium Price
Primary Message: Busy Schedule? (Photo of Male or Female Pharmacist)
Secondary Message: Let Us Make Ordering Pharmacy Vials Easy For You!
EASY and CONVENIENT
ORDER ONLINE ktrservices.example
ORDER BY PHONE 888-413-5276
ORDER BY FAX 855-307-4182
KTR Services’ line of pharmacy vials, bottles and jars brings you the highest quality products at the lowest prices.
Graphic Element or Call Out: High quality, low prices, great customer service, free shipping (over $90) and a vast inventory selection
Vials

Jars and Liquid

Can’t find a particular product? Call Us and we will do everything to get the product for you. We want to be your source for pharmacy vials and toner supplies.
To place an order, or receive additional information and pricing please contact our customer service representatives at customer@ktrservices.example, online chat at ktrservices.example or 888-413-5276.

Back Side:
Graphic Element Needed: The more you need, the more you save.
The more you buy, earn higher discounts. You receive a 5% discount on every three cases purchased, up to 12% discount.
Mix and match quantities include all vials, bottles and jars, all type caps!
Everyday Quantity Discounts (Mix and Match Your Order)
(Graphic Element or call outs for below)
5% for every three (3) cases
8% for every six (6) cases
12% for every eleven (11) plus cases
Graphic Element Needed - Gift Card or KTR Store Credit for Your Referrals
KTR Services knows the importance of our customers. We know that if you have a great experience with us, and refer us to another customer, we want to reward you for your referrals. For every customer you refer to us that makes a purchase. The more you refer, the more you can earn. Call us today at 888-413-5276.
You can view our line of pharmacy vials and ink & toner products on www.ktrservices.example.

ORDER BY FAX 855-307-4182

Please call 888-413-5276 for Vial Samples, Vials and Toner Bundle Pricing & Additional Information.

Industry/Entity Type

It Company

Requirements
Must have
• Use Logo Attached
Should not have
• clipart illustrations of dollar bills

```html
<!DOCTYPE html>
<html lang="en">
<head>
<meta charset="utf-8">
<title>KTR Services – Pharmacy Vials Sales Sheet</title>
<link rel="stylesheet" href="https://fonts.googleapis.com/css2?family=Cinzel:wght@500&family=Roboto+Condensed:wght@400;700&family=Arimo:ital,wght@0,400;0,700;1,700&family=Questrial&family=Barlow:wght@500;600&display=swap">
<style>
  :root {
    --bg: #e9e6e1;
    --paper: #fbfcf7;
    --paper-edge: #eef3e3;
    --blue: #1b8ccb;
    --blue-dark: #14679f;
    --navy: #2a3296;
    --green: #1f9a3e;
    --green-dark: #0d7a35;
    --green-light: #7cc242;
    --text-green: #1b6a2a;
    --ink: #222;
  }
  * { box-sizing: border-box; margin: 0; padding: 0; }
  html, body { width: 1200px; height: 770px; overflow: hidden; }
  body { background: var(--bg); position: relative; font-family: "Arimo", Arial, sans-serif; }

  .sheet {
    position: absolute; top: 28px; width: 552px; height: 714px;
    background: radial-gradient(ellipse at 50% 50%, var(--paper) 60%, var(--paper-edge) 100%);
    box-shadow: 0 2px 8px rgba(0,0,0,.18);
    overflow: hidden;
  }
  .sheet--front { left: 32px; }
  .sheet--back { left: 616px; }
  .abs { position: absolute; }

  .brand { display: flex; flex-direction: column; align-items: center; gap: 8px; }
  .brand__dot { width: 34px; height: 34px; border-radius: 50%; background: var(--blue-dark); }
  .brand__name { font-family: "Roboto Condensed", sans-serif; font-weight: 700; font-size: 15px; color: var(--navy); white-space: nowrap; }

  .accent-bar { background: var(--green-light); height: 8px; }
  .title-banner {
    background: linear-gradient(90deg, var(--blue) 0%, #2ba3dc 100%);
    height: 32px; display: flex; align-items: center;
    font-family: "Cinzel", serif; font-weight: 500; color: #fff; font-size: 15px; letter-spacing: .2px;
    white-space: nowrap; overflow: hidden;
  }
  .title-underline { background: var(--green); height: 7px; }

  .photo {
    left: 202px; top: 114px; width: 350px; height: 200px;
    background: linear-gradient(100deg, #e4e7ea 0%, #f3f1ee 35%, #f8f6f3 55%, #dde3ea 100%);
  }

  .headline { font-family: "Arimo", sans-serif; font-weight: 700; color: var(--blue-dark); font-size: 26px; line-height: 30px; }
  .subhead { font-weight: 700; color: var(--navy); font-size: 12px; line-height: 14.5px; }

  .band-piece { height: 24px; }
  .band-label { color: #fff; font-family: "Arimo", sans-serif; font-size: 15px; display: flex; align-items: center; justify-content: center; }

  .order-list { font-family: "Barlow", sans-serif; font-size: 14px; line-height: 17.5px; color: var(--text-green); }
  .order-list div { display: flex; }
  .order-list dt { width: 126px; font-weight: 500; }
  .order-list dd { font-weight: 600; color: var(--green-dark); white-space: nowrap; }

  .promise { font-style: italic; font-weight: 700; color: var(--navy); font-size: 13px; line-height: 17px; text-align: center; }

  .callout-band { color: #fff; font-family: "Roboto Condensed", sans-serif; font-weight: 700; font-size: 19.5px; line-height: 25px; text-align: center; display: flex; align-items: center; justify-content: center; }
  .grey-wedge { background: linear-gradient(90deg, #6f7f8f, #d9dee3); }

  .body-copy { font-family: "Questrial", sans-serif; font-size: 13.5px; line-height: 16.5px; color: var(--ink); text-align: justify; }
  .body-copy p + p { margin-top: 15px; }
  .body-copy b { font-family: "Arimo", sans-serif; font-weight: 700; }

  .foot-bar { height: 14px; top: 700px; }

  .discount-lead { font-weight: 700; color: var(--navy); font-size: 14px; line-height: 26px; text-align: center; }
  .discount-lead big { font-size: 21px; }
  .mix-note { font-weight: 700; color: var(--green-dark); font-size: 15px; line-height: 20px; text-align: center; }
  .everyday { font-family: "Questrial", sans-serif; color: var(--blue-dark); font-size: 19px; font-weight: 700; text-align: center; white-space: nowrap; }
  .everyday small { font-size: 15px; }
  .tiers { color: #fff; font-family: "Roboto Condensed", sans-serif; font-weight: 700; font-size: 20.5px; line-height: 25px; text-align: right; white-space: nowrap; }
  .referral-title { font-family: "Questrial", sans-serif; font-weight: 700; color: var(--navy); font-size: 16.5px; line-height: 21.5px; }
  .gift-art {
    background: linear-gradient(110deg, #2f49b8 0%, #4b3fa8 40%, #b43b8e 60%, #e8362b 78%, #f28a1c 100%);
    border-radius: 10px; transform: rotate(-8deg);
  }
  .small-copy { font-family: "Questrial", sans-serif; font-size: 12px; line-height: 15.2px; color: var(--ink); text-align: justify; }
  .small-copy p + p { margin-top: 12px; }
  .small-copy b { font-family: "Arimo", sans-serif; font-weight: 700; font-size: 13px; }
</style>
</head>
<body>

<section class="sheet sheet--front">
  <div class="abs brand" style="left:30px;top:40px;width:100px;">
    <span class="brand__dot"></span>
    <span class="brand__name">KTR Services, LLC.</span>
  </div>

  <div class="abs accent-bar" style="left:356px;top:50px;width:196px;"></div>
  <div class="abs title-banner" style="left:140px;top:62px;width:412px;padding-left:26px;clip-path:polygon(0 0,100% 0,100% 100%,16px 100%);">Quality Vials without the Premium Price</div>
  <div class="abs title-underline" style="left:160px;top:97px;width:148px;"></div>

  <div class="abs photo" role="img" aria-label="Smiling pharmacist in a white coat in front of pharmacy shelves"></div>

  <h1 class="abs headline" style="left:34px;top:178px;">Busy<br>Schedule?</h1>
  <p class="abs subhead" style="left:34px;top:252px;">Let Us Make Ordering<br>Pharmacy Vials Easy<br>For You!</p>

  <div class="abs band-piece" style="left:0;top:322px;width:120px;background:linear-gradient(90deg,var(--green-light),var(--green));clip-path:polygon(0 0,92% 0,100% 100%,0 100%);"></div>
  <div class="abs band-piece" style="left:118px;top:322px;width:350px;background:linear-gradient(90deg,var(--blue-dark),var(--blue));clip-path:polygon(0 0,100% 0,98% 100%,3% 100%);"></div>
  <div class="abs band-piece band-label" style="left:118px;top:322px;width:350px;">EASY and CONVENIENT</div>
  <div class="abs band-piece" style="left:432px;top:322px;width:120px;background:linear-gradient(90deg,var(--green),var(--green-light));clip-path:polygon(6% 0,100% 0,100% 100%,0 100%);"></div>

  <dl class="abs order-list" style="left:34px;top:368px;">
    <div><dt>ORDER ONLINE</dt><dd>ktrservices.example</dd></div>
    <div><dt>ORDER BY PHONE</dt><dd>888-413-5276</dd></div>
    <div><dt>ORDER BY FAX</dt><dd>855-307-4182</dd></div>
  </dl>
  <p class="abs promise" style="left:300px;top:362px;width:216px;">KTR Services’ line of pharmacy vials, bottles and jars brings you the highest quality products at the lowest prices.</p>

  <div class="abs grey-wedge" style="left:0;top:444px;width:70px;height:100px;clip-path:polygon(0 0,20% 0,100% 100%,0 100%);"></div>
  <div class="abs callout-band" style="left:28px;top:444px;width:496px;height:100px;background:linear-gradient(90deg,var(--green-dark),var(--green) 60%,#2aa34a);clip-path:polygon(0 0,96% 0,100% 100%,6% 100%);">High quality, low prices,<br>great customer service, free shipping (over $90)<br>and a vast inventory selection Vials</div>
  <div class="abs grey-wedge" style="left:480px;top:444px;width:72px;height:100px;clip-path:polygon(0 0,100% 0,100% 100%,42% 100%);background:linear-gradient(90deg,#c8d0d8,#7b8997);"></div>

  <div class="abs body-copy" style="left:34px;top:556px;width:480px;">
    <p>Can’t find a particular product? Call Us and we will do everything to get the product for you. We want to be your source for pharmacy vials and toner supplies.</p>
    <p>To place an order, or receive additional information and pricing please contact our customer service representatives at <b>customer@ktrservices.example</b>, online chat at <b>ktrservices.example</b> or <b>888-413-5276</b>.</p>
  </div>

  <div class="abs foot-bar" style="left:0;width:200px;background:var(--blue);clip-path:polygon(0 0,94% 0,100% 100%,0 100%);"></div>
  <div class="abs foot-bar" style="left:164px;width:388px;background:linear-gradient(90deg,var(--green),var(--green-light));clip-path:polygon(0 0,100% 0,100% 100%,3% 100%);"></div>
</section>

<section class="sheet sheet--back">
  <div class="abs accent-bar" style="left:0;top:50px;width:196px;"></div>
  <div class="abs title-banner" style="left:0;top:62px;width:412px;padding-left:24px;font-size:16px;clip-path:polygon(0 0,100% 0,calc(100% - 16px) 100%,0 100%);">The More You Need, the More You Save</div>
  <div class="abs title-underline" style="left:244px;top:97px;width:148px;"></div>
  <div class="abs brand" style="left:424px;top:40px;width:100px;">
    <span class="brand__dot"></span>
    <span class="brand__name">KTR Services, LLC.</span>
  </div>

  <p class="abs discount-lead" style="left:0;top:140px;width:552px;">The more you buy, earn higher discounts. You receive a<br><big>5% discount</big> on every three cases purchased,<br>up to <big>12% discount</big>.</p>
  <p class="abs mix-note" style="left:0;top:232px;width:552px;">Mix and match quantities include all vials,<br>bottles and jars, all type caps!</p>
  <p class="abs everyday" style="left:0;top:286px;width:552px;">Everyday Quantity Discounts <small>(Mix and Match Your Order)</small></p>

  <div class="abs" style="left:0;top:322px;width:160px;height:24px;background:linear-gradient(90deg,#9aa6b2,#5f6f7f);"></div>
  <div class="abs" style="left:156px;top:322px;width:396px;height:96px;background:linear-gradient(90deg,var(--green),var(--green-dark) 70%);clip-path:polygon(0 0,100% 0,100% 100%,10% 100%);"></div>
  <div class="abs tiers" style="left:200px;top:330px;width:318px;">5% for every three (3) cases<br>8% for every six (6) cases<br>12% for every eleven (11) plus cases</div>

  <h2 class="abs referral-title" style="left:36px;top:396px;">Gift Card or<br>KTR Store Credit<br>for Your Referrals</h2>
  <div class="abs gift-art" role="img" aria-label="Fanned stack of colourful gift cards in several values" style="left:44px;top:496px;width:172px;height:98px;"></div>

  <div class="abs small-copy" style="left:254px;top:430px;width:262px;">
    <p>KTR Services knows the importance of our customers. We know that if you have a great experience with us, and refer us to another customer, we want to reward you for your referrals. For every customer you refer to us that makes a purchase. The more you refer, the more you can earn. Call us today at <b>888-413-5276</b>.</p>
    <p>You can view our line of pharmacy vials and ink &amp; toner products on <b>www.ktrservices.example</b>.</p>
  </div>

  <dl class="abs order-list" style="left:36px;top:640px;">
    <div><dt>ORDER ONLINE</dt><dd>ktrservices.example</dd></div>
    <div><dt>ORDER BY PHONE</dt><dd>888-413-5276</dd></div>
    <div><dt>ORDER BY FAX</dt><dd>855-307-4182</dd></div>
  </dl>
  <p class="abs small-copy" style="left:298px;top:642px;width:218px;">Please call <b>888-413-5276</b> for Vial Samples, Vials and Toner Bundle Pricing &amp; Additional Information.</p>

  <div class="abs foot-bar" style="left:0;width:530px;background:linear-gradient(90deg,var(--green),var(--green-light));clip-path:polygon(0 0,97% 0,100% 100%,0 100%);"></div>
  <div class="abs foot-bar" style="left:516px;width:36px;background:var(--blue);clip-path:polygon(0 0,100% 0,100% 100%,40% 100%);"></div>
</section>

</body>
</html>
```